Poster of Core Values & Motto

Create our core values poster and motto. Attached are our core values and our Motto. This poster represents both of our companies Tidy Pulp & CuraBinix.

Target Market(s)

Our team / employees

Industry/Entity Type

Shredding and Medical Waste

Colors
59FF00
82FF00
B8FF75
E3FFCB
F4FFEA
EB3D1F
EC4F4E
F09395
F8D3D4
FCEDEE

Requirements
Must have
• Include both companies logos

```html
<!DOCTYPE html>
<html lang="en">
<head>
<meta charset="utf-8">
<title>Core Values Poster – Tidy Pulp &amp; CuraBinix</title>
<link href="https://fonts.googleapis.com/css2?family=League+Spartan:wght@700&family=Montserrat:wght@400;500;700&display=swap" rel="stylesheet">
<style>
  :root{
    --green:#079a3c;
    --olive:#8a7f2e;
    --orange:#c65a25;
    --red:#e0201f;
    --value-green:#7dbb3f;
    --value-green-deep:#5fae3a;
    --value-red:#d82a2a;
    --motto:#1da34b;
    --paper:#ffffff;
  }
  *{margin:0;padding:0;box-sizing:border-box}
  html,body{width:848px;height:1200px;overflow:hidden;background:var(--paper)}
  body{font-family:"Montserrat",Arial,sans-serif}
  .poster{
    position:relative;width:848px;height:1200px;
    background:linear-gradient(90deg,var(--green) 0%,var(--olive) 45%,var(--orange) 75%,var(--red) 100%);
  }
  .poster__sheet{
    position:absolute;left:30px;top:36px;right:30px;bottom:8px;background:var(--paper);
  }
  .value{position:absolute;font-size:16.5px;line-height:21px;white-space:nowrap}
  .value__title{display:block;font-weight:700;letter-spacing:.2px}
  .value__line{display:block;font-weight:500}
  .value--green{color:var(--value-green)}
  .value--deep{color:var(--value-green-deep)}
  .value--red{color:var(--value-red)}
  .value--top-left{left:38px;top:43px}
  .value--top-right{right:43px;top:43px;text-align:right}
  .value--side{transform-origin:0 0;transform:rotate(-90deg)}
  .value--efficient{left:37px;top:652px}
  .value--synergy{left:37px;top:1142px}
  .value--secure{left:767px;top:640px}
  .value--dependable{left:767px;top:1142px}

  .motto-words{position:absolute;left:0;top:0;width:848px;height:1200px}
  .motto{
    position:absolute;left:0;right:0;top:928px;text-align:center;
    color:var(--motto);font-weight:700;font-size:20.5px;line-height:28px;letter-spacing:.2px
  }
  .brand{
    position:absolute;top:1066px;display:flex;align-items:center;gap:10px;
    font-weight:700;font-size:26px;line-height:1
  }
  .brand__dot{width:22px;height:22px;border-radius:50%}
  .brand--pulp{left:200px;color:var(--green)}
  .brand--pulp .brand__dot{background:var(--green)}
  .brand--cura{left:462px;color:var(--red)}
  .brand--cura .brand__dot{background:var(--red);border-radius:0}
</style>
</head>
<body>
<main class="poster">
  <div class="poster__sheet"></div>

  <p class="value value--green value--top-left"><span class="value__title">EXELLANCE</span><span class="value__line">Exceed with a smile</span></p>
  <p class="value value--red value--top-right"><span class="value__title">HONESTY/INTEGRITY</span><span class="value__line">Do the right thing</span></p>

  <p class="value value--side value--green value--efficient"><span class="value__title">EFFICIENT</span><span class="value__line">On-Time, sence of urgency, always trying to improve</span></p>
  <p class="value value--side value--deep value--synergy"><span class="value__title">SYNERGY/TEAMWORK</span><span class="value__line">Get It Done Attitude with Humble confidence</span></p>
  <p class="value value--side value--red value--secure"><span class="value__title">SAFE AND SECURE</span><span class="value__line">We are just as secure as an armored truck with money</span></p>
  <p class="value value--side value--red value--dependable"><span class="value__title">DEPENDABLE</span><span class="value__line">Do what you say you will do</span></p>

  <svg class="motto-words" viewBox="0 0 848 1200" aria-label="Purpose, Cause, Passion">
    <defs>
      <linearGradient id="wordsGradient" x1="215" y1="0" x2="630" y2="0" gradientUnits="userSpaceOnUse">
        <stop offset="0" stop-color="#079a3c"/>
        <stop offset="0.45" stop-color="#8a7f2e"/>
        <stop offset="0.75" stop-color="#c65a25"/>
        <stop offset="1" stop-color="#e0201f"/>
      </linearGradient>
      <clipPath id="wordsClip">
        <text transform="translate(322 892) rotate(-90)" font-family="League Spartan, Arial, sans-serif" font-weight="700" font-size="150" textLength="790" lengthAdjust="spacingAndGlyphs">PURPOSE</text>
        <text transform="translate(457 892) rotate(-90)" font-family="League Spartan, Arial, sans-serif" font-weight="700" font-size="176" textLength="548" lengthAdjust="spacingAndGlyphs">CAUSE</text>
        <text transform="translate(627 892) rotate(-90)" font-family="League Spartan, Arial, sans-serif" font-weight="700" font-size="212" textLength="722" lengthAdjust="spacingAndGlyphs">PASSION</text>
      </clipPath>
    </defs>
    <rect x="200" y="90" width="440" height="810" fill="url(#wordsGradient)" clip-path="url(#wordsClip)"/>
  </svg>

  <p class="motto">REMIND PEOPLE<br>WHAT GREAT SERVICE LOOKS LIKE</p>

  <div class="brand brand--pulp"><span class="brand__dot"></span><span class="brand__name">Tidy Pulp</span></div>
  <div class="brand brand--cura"><span class="brand__dot"></span><span class="brand__name">CuraBinix</span></div>
</main>
</body>
</html>
```